Banner for promote service of debit card

We are PagoVela and we need the banners to be posted on the facebook and instagram pages.
We want something to communicate that it is an exclusive debit card full of services.
Low commissions.
Our competitors:
https://www.kelvopay.com/it/home.html
https://www.drolo.com/it/
https://www.fotoreelix.com/sereqobank/
zephrolinko
maybe some banner that makes the idea of a convenient debit card that everyone can use.
Girls enjoying card shopping.
Please check also website for slogans and phrases to use
https://www.pagovela-app.com/
Should show the services.
We must convey that it is a fast, simple card that guarantees privacy.
We need strong banners that attract people as these ban will be sponsored on instagram and facebook
Target Market(s)
People 18-35 y
Open Bank account. low commissions. Easy to use. No limits. 100% Privacy.
Requirements
Must have
- Written in Italian.

```html
<!DOCTYPE html>
<html lang="it">
<head>
<meta charset="utf-8">
<title>PagoVela – Una carta per tutti</title>
<link rel="stylesheet" href="https://fonts.googleapis.com/css2?family=Ubuntu:wght@400;500;700&display=swap">
<style>
  :root {
    --page-bg: #eef0f4;
    --blue-deep: #2b3fc9;
    --blue-mid: #3f5be0;
    --violet: #5a34c8;
    --magenta: #e8287a;
    --pink: #ff3f8e;
    --orange: #ff8a3d;
    --yellow: #ffd43b;
    --cyan: #62d4f4;
    --lilac: #8a6cf2;
    --white: #ffffff;
    --soft-white: rgba(255,255,255,0.85);
  }
  * { box-sizing: border-box; margin: 0; padding: 0; }
  html, body { width: 1200px; height: 800px; overflow: hidden; }
  body {
    background: var(--page-bg);
    font-family: "Ubuntu", sans-serif;
    display: flex;
    align-items: center;
    justify-content: center;
  }
  .banner {
    position: relative;
    width: 740px;
    height: 740px;
    overflow: hidden;
    background: linear-gradient(160deg, var(--blue-mid) 0%, var(--blue-deep) 55%, var(--violet) 100%);
    box-shadow: 0 10px 30px rgba(20, 30, 80, 0.18);
  }
  .banner__stripes { position: absolute; inset: 0; width: 100%; height: 100%; }
  .headline { position: absolute; left: 36px; top: 60px; }
  .headline__kicker { color: var(--yellow); font-weight: 700; font-size: 30px; line-height: 1.15; }
  .headline__title { color: var(--white); font-weight: 700; font-size: 30px; line-height: 1.2; }
  .follow { position: absolute; right: 30px; top: 62px; text-align: right; }
  .follow__label { color: var(--yellow); font-weight: 700; font-size: 19px; }
  .follow__dots { display: flex; gap: 8px; justify-content: flex-end; margin-top: 8px; }
  .follow__dot { width: 20px; height: 20px; border-radius: 50%; background: var(--white); }
  .illustration {
    position: absolute; left: 150px; top: 165px; width: 450px; height: 370px;
    border-radius: 32px;
    background: linear-gradient(135deg, var(--cyan) 0%, var(--lilac) 48%, var(--pink) 100%);
    box-shadow: 0 24px 40px rgba(30, 20, 110, 0.35);
  }
  .benefits {
    position: absolute; left: 36px; top: 560px; list-style: none;
    color: var(--white); font-size: 19px; line-height: 1.55; font-weight: 500;
  }
  .cta {
    position: absolute; left: 36px; top: 665px;
    background: var(--magenta); color: var(--white);
    font-weight: 700; font-size: 15px;
    padding: 8px 22px; border-radius: 20px;
  }
  .site-url {
    position: absolute; left: 500px; top: 575px; width: 200px; text-align: center;
    color: var(--soft-white); font-size: 15px; font-weight: 500;
    transform: rotate(-50deg);
  }
  .brand {
    position: absolute; right: 30px; bottom: 40px;
    display: flex; align-items: center; gap: 8px;
    color: var(--white); font-weight: 500; font-size: 20px;
  }
  .brand__mark { width: 18px; height: 18px; border-radius: 50%; background: var(--white); }
</style>
</head>
<body>
  <section class="banner">
    <svg class="banner__stripes" viewBox="0 0 740 740" aria-hidden="true">
      <defs>
        <linearGradient id="stripe-warm" x1="0" y1="0" x2="1" y2="1">
          <stop offset="0" stop-color="#ff8a3d"/>
          <stop offset="1" stop-color="#e8287a"/>
        </linearGradient>
      </defs>
      <polygon points="0,0 150,0 0,180" fill="#7b3fd4" opacity="0.7"/>
      <polygon points="0,150 125,0 145,0 0,175" fill="url(#stripe-warm)"/>
      <polygon points="0,210 175,0 185,0 0,222" fill="#ff3f8e" opacity="0.8"/>
      <polygon points="740,520 740,740 550,740" fill="#7b3fd4" opacity="0.7"/>
      <polygon points="740,470 740,500 520,740 490,740" fill="url(#stripe-warm)"/>
      <polygon points="740,560 740,580 590,740 570,740" fill="#ff3f8e"/>
      <polygon points="740,620 740,740 640,740" fill="#e8287a" opacity="0.85"/>
    </svg>

    <header class="headline">
      <p class="headline__kicker">All In One!</p>
      <h1 class="headline__title">Una carta per tutti</h1>
    </header>

    <div class="follow">
      <p class="follow__label">Follow us</p>
      <div class="follow__dots"><span class="follow__dot"></span><span class="follow__dot"></span></div>
    </div>

    <div class="illustration" role="img" aria-label="Illustrazione isometrica: smartphone con carta di credito, regali, borse della spesa e persone che acquistano online"></div>

    <ul class="benefits">
      <li>Nessun limite</li>
      <li>Nessun controllo</li>
      <li>Tutto quello che vuoi</li>
    </ul>

    <p class="cta">Ottieni la tua Carta</p>

    <p class="site-url">www.pagovela-app.com</p>

    <div class="brand"><span class="brand__mark"></span><span>PagoVela</span></div>
  </section>
</body>
</html>
```